Stationery Design Project

Need stationery designed for our chicken farming business. We grow chickens in barns for meat production. Looking for all stationery items (business cards, letterhead, envelopes, with compliments etc).
Updates

Reason: I am going away for 5 days from Friday 30/3/2012. Won't be able to check designs.

Target Market(s)

The stationery will only be used for correspondence with key stakeholders / suppliers. It is not to be used for marketing etc.

Industry/Entity Type

Business

Requirements
Must have
• I have included all the contact details required for each type of stationery.
Nice to have
• Colours to be used white, green, red, yellow and black (see design).
Should not have
• Rounded Corners.
Centralised information (in centre of business cards / letterhead etc).

```html
<!DOCTYPE html>
<html lang="en">
<head>
<meta charset="utf-8">
<title>Brookvale Poultry Stationery</title>
<link href="https://fonts.googleapis.com/css2?family=Arimo:wght@400;700&display=swap" rel="stylesheet">
<style>
  :root {
    --page-bg: #ecebe8;
    --paper: #ffffff;
    --green: #1f6749;
    --green-dark: #17573c;
    --red: #9b1c20;
    --red-bright: #e3262b;
    --yellow: #f6b21a;
    --ink: #1a1a1a;
    --chick-light: #f7efd2;
    --chick-mid: #e9d49a;
  }
  * { box-sizing: border-box; margin: 0; padding: 0; }
  html, body { width: 1200px; height: 822px; overflow: hidden; }
  body {
    background: var(--page-bg);
    font-family: "Arimo", Arial, sans-serif;
    color: var(--ink);
    position: relative;
  }
  .sheet {
    position: absolute;
    background: var(--paper);
    box-shadow: 0 2px 6px rgba(0,0,0,0.18);
    overflow: hidden;
  }
  .letterhead { left: 46px; top: 35px; width: 526px; height: 743px; }
  .envelope-front { left: 599px; top: 119px; width: 571px; height: 255px; }
  .envelope-back { left: 599px; top: 440px; width: 571px; height: 254px; }

  .shape { position: absolute; display: block; }

  .contact-list {
    position: absolute;
    list-style: none;
    font-size: 6.6px;
    line-height: 9.2px;
  }
  .contact-list li { display: flex; align-items: flex-start; gap: 5px; }
  .contact-icon {
    flex: 0 0 auto;
    width: 5px; height: 5px;
    margin-top: 2px;
    border-radius: 50%;
    background: var(--yellow);
  }
  .contact-icon.blank { background: none; }

  .brand {
    position: absolute;
    display: flex;
    align-items: center;
    gap: 8px;
    color: var(--ink);
    font-weight: 700;
  }
  .brand-dot {
    flex: 0 0 auto;
    width: 34px; height: 34px;
    border-radius: 50%;
    background: var(--red);
  }
  .brand-name { line-height: 1; }
  .brand-name .line-main { display: block; font-size: 25px; }
  .brand-name .line-sub { display: block; font-size: 13px; margin-top: 3px; padding-left: 18px; }

  .chicks-photo {
    position: absolute;
    background: radial-gradient(ellipse at 50% 45%, var(--chick-light) 0%, var(--chick-mid) 60%, rgba(233,212,154,0) 100%);
  }

  .envelope-top-strip {
    position: absolute; left: 0; top: 0; width: 100%; height: 12px;
    background: var(--green);
  }
</style>
</head>
<body>

<section class="sheet letterhead" aria-label="Letterhead">
  <svg class="shape" style="left:0;top:34px" width="42" height="56" viewBox="0 0 42 56">
    <path d="M0 0 H42 C30 14 30 42 42 56 H0 Z" fill="var(--red)"/>
  </svg>

  <ul class="contact-list" style="left:52px;top:39px">
    <li><span class="contact-icon"></span>(111) 555 014 206</li>
    <li><span class="contact-icon"></span>(111) 555 014 206</li>
    <li><span class="contact-icon"></span>info@brookvalepoultry.com</li>
    <li><span class="contact-icon"></span>www.brookvalepoultry.com</li>
    <li><span class="contact-icon"></span>22,23,24, XXXX Floor,</li>
    <li><span class="contact-icon blank"></span>XXXX Centre, City, Country</li>
  </ul>

  <div class="brand" style="left:205px;top:36px">
    <span class="brand-dot"></span>
    <span class="brand-name"><span class="line-main">Brookvale</span><span class="line-sub">Poultry Pty Ltd</span></span>
  </div>

  <svg class="shape" style="left:424px;top:27px" width="102" height="68" viewBox="0 0 102 68">
    <defs>
      <linearGradient id="bandGradLetter" x1="0" y1="0" x2="1" y2="0">
        <stop offset="0" stop-color="var(--yellow)"/>
        <stop offset="0.45" stop-color="#7f8a4c"/>
        <stop offset="1" stop-color="var(--green)"/>
      </linearGradient>
    </defs>
    <path d="M28 0 H102 V68 H0 C18 50 26 26 28 0 Z" fill="url(#bandGradLetter)"/>
    <path d="M28 0 C26 26 18 50 0 68 H6 C22 50 30 26 34 0 Z" fill="var(--red-bright)"/>
  </svg>

  <div class="chicks-photo" role="img" aria-label="Photo of two young chicks standing together" style="left:420px;top:639px;width:95px;height:92px"></div>
</section>

<section class="sheet envelope-front" aria-label="Envelope front">
  <div class="envelope-top-strip"></div>

  <svg class="shape" style="left:0;top:202px" width="38" height="53" viewBox="0 0 38 53">
    <path d="M0 0 H38 C27 13 27 40 38 53 H0 Z" fill="var(--red)"/>
  </svg>

  <ul class="contact-list" style="left:43px;top:205px;font-size:6.2px;line-height:7.4px">
    <li><span class="contact-icon"></span>(111) 555 014 206</li>
    <li><span class="contact-icon"></span>(111) 555 014 206</li>
    <li><span class="contact-icon"></span>info@brookvalepoultry.com</li>
    <li><span class="contact-icon"></span>www.brookvalepoultry.com</li>
    <li><span class="contact-icon"></span>22,23,24, XXXX Floor,</li>
    <li><span class="contact-icon blank"></span>XXXX Centre, City, Country</li>
  </ul>

  <div class="chicks-photo" role="img" aria-label="Photo of two young chicks standing together" style="left:195px;top:204px;width:48px;height:45px"></div>

  <div class="brand" style="left:294px;top:206px">
    <span class="brand-dot"></span>
    <span class="brand-name"><span class="line-main">Brookvale</span><span class="line-sub">Poultry Pty Ltd</span></span>
  </div>

  <svg class="shape" style="left:488px;top:198px" width="83" height="57" viewBox="0 0 83 57">
    <defs>
      <linearGradient id="bandGradEnvelope" x1="0" y1="0" x2="1" y2="0">
        <stop offset="0" stop-color="var(--yellow)"/>
        <stop offset="0.45" stop-color="#7f8a4c"/>
        <stop offset="1" stop-color="var(--green)"/>
      </linearGradient>
    </defs>
    <path d="M22 0 H83 V57 H0 C14 42 20 22 22 0 Z" fill="url(#bandGradEnvelope)"/>
    <path d="M22 0 C20 22 14 42 0 57 H6 C18 42 25 22 28 0 Z" fill="var(--red-bright)"/>
  </svg>
</section>

<section class="sheet envelope-back" aria-label="Envelope back">
  <svg class="shape" style="left:0;top:0" width="571" height="54" viewBox="0 0 571 54">
    <path d="M0 0 H571 V16 C571 36 560 54 540 54 H31 C11 54 0 36 0 16 Z" fill="var(--green)"/>
  </svg>
</section>

</body>
</html>
```